Bright Meridian Partners boutique mgt consulting group 5 page web design

I need a 4 - 5 page website that professionally presents the business and what we do/ offer to potential clients. We are a boutique based consultancy business that is cutting edge, focuses on revenue and profit acceleration for our customers primarily focused on (but looking to expand outside of ) the consumer goods and property/ building markets. We are passionate about seeing our clients grow their business and our Experts are not traditional consultants, rather are senior executive experts that specialise in sales, marketing, leadership, coaching, supply chain functions at C suite and below.

I have just had a new logo created and so would like to replicate this feel through the website please.

The final Website design needs to communicate a new era of consulting and freelance experts where technology will support our offer.. it needs to be be on trend, animated, modern, professional and primarily researched by clients on their mobile devices. Whilst a consultancy I don't want our clients to feel it looks the same as a traditional consultancy...

Videos will be added later.

For basic content feel please see existing www.brightmeridianpartners.example website.
I would expect a landing page, our services, about us/ who we are, clients we work with.

The type of website I like the feel of is:
http://cartlumen.example.com.au

Target Market(s)

Business to Business Manufacturers/ Retailers/ Property

Industry/Entity Type

Management Consulting

Coding

Coded - Design and coding required

Number of Pages Required

5+ page

Font styles to use
Sans Serif

Colors

Designer to choose colors to be used in the design.

Requirements
Must have
• 5 pages including landing page, our services, about us/ who we are, clients we work with.
• Modern, professional look
• demonstrate the services
• ability to add video and content later
• Use the logo
• ability to scroll and look up on mobile devices
Nice to have
• Use my logo as watermark
• Moving images
• I like this website:
• https://trovanix.example
• http://cartlumen.example.com.au
• other websites :
• https://skillharbor.example
Should not have
• The look of a traditional Big 4 consulting firm
• Be fixed and static website

```html
<!DOCTYPE html>
<html lang="en">
<head>
<meta charset="utf-8">
<title>Bright Meridian Partners</title>
<link href="https://fonts.googleapis.com/css2?family=Open+Sans:ital,wght@0,300;0,400;0,600;0,700;1,400&display=swap" rel="stylesheet">
<style>
:root{
  --blue:#1f65b3;
  --blue-bright:#2b7bd0;
  --navy:#0f2d5a;
  --navy-deep:#0a2247;
  --ink:#4a5563;
  --muted:#8a94a3;
  --grey-band:#dfe3e8;
  --white:#ffffff;
}
*{margin:0;padding:0;box-sizing:border-box}
html,body{width:1200px;height:3128px;overflow:hidden}
body{position:relative;font-family:"Open Sans",Arial,sans-serif;color:var(--ink);background:var(--white)}
.abs{position:absolute}
.center{text-align:center}

/* hero */
.hero{left:0;top:0;width:1200px;height:640px;background:linear-gradient(160deg,#3d6fa8 0%,#6f93bd 40%,#2d5d98 75%,#1d4a86 100%)}
.hero-notch{left:0;top:540px;width:1200px;height:110px}
.topbar-phone{right:44px;top:28px;color:var(--white);font-size:18px;font-weight:600;display:flex;align-items:center;gap:8px}
.brand{left:150px;top:34px;display:flex;align-items:center;gap:12px;color:var(--white);font-weight:700;font-size:19px;letter-spacing:.5px}
.brand-dot{width:22px;height:22px;border-radius:50%;background:var(--white)}
.nav{right:40px;top:76px;display:flex;gap:30px;align-items:center;color:var(--white);font-size:15px;font-weight:600;letter-spacing:.5px}
.nav .active{border-bottom:2px solid var(--white);padding-bottom:4px}
.hero-title{left:0;top:262px;width:1200px;color:var(--white);font-size:54px;font-weight:400}
.hero-sub{left:0;top:340px;width:1200px;color:var(--white);font-size:20px}
.btn-outline{left:530px;top:384px;width:140px;height:44px;border:2px solid var(--white);color:var(--white);font-size:15px;line-height:40px;text-align:center;letter-spacing:.5px}

/* welcome */
.welcome-mark{left:584px;top:618px;width:32px;height:32px;border-radius:50%;background:var(--blue)}
.section-title{left:0;width:1200px;color:var(--blue);font-size:38px;font-weight:700;text-align:center}
.welcome-title{top:676px}
.welcome-copy{left:220px;top:744px;width:760px;font-size:15px;line-height:26px;text-align:center}
.welcome-copy p{margin-bottom:18px}
.btn-solid{left:500px;top:904px;width:200px;height:56px;background:var(--navy);color:var(--white);font-size:17px;line-height:56px;text-align:center;letter-spacing:.5px}

/* expertise */
.expert{left:0;top:1022px;width:1200px;height:386px;background:linear-gradient(135deg,#1b4f94 0%,#2b6fbc 50%,#1a4a8c 100%)}
.expert-title{left:0;top:1060px;width:1200px;color:var(--white);font-size:40px;font-weight:700;text-align:center}
.skill{top:1180px;width:170px;text-align:center;color:var(--white);font-weight:700;font-size:16px;letter-spacing:.5px}
.skill-icon{width:124px;height:124px;border-radius:50%;background:var(--white);margin:0 auto 32px;display:flex;align-items:center;justify-content:center}

/* quote */
.quote-band{left:0;top:1408px;width:1200px;height:214px;background:linear-gradient(180deg,#c9ced4 0%,#eef0f2 45%,#b9bfc6 100%)}
.quote-mark{left:170px;top:1440px;font-size:140px;color:var(--white);font-weight:700;line-height:1}
.quote-text{left:340px;top:1470px;width:560px;font-size:21px;font-style:italic;color:#505a66;line-height:32px}
.quote-author{right:60px;top:1570px;font-size:15px;color:#505a66}
.arrow{width:30px;height:50px}

/* services */
.services-title{top:1668px}
.services-sub{left:0;top:1728px;width:1200px;font-size:14px;color:var(--muted);text-align:center}
.services-copy{left:200px;top:1778px;width:800px;font-size:14px;line-height:24px;text-align:center;color:var(--muted)}
.tile{top:1888px;width:400px;height:304px}
.tile-label{top:2192px;width:400px;height:48px;background:var(--navy);color:var(--white);font-size:16px;font-weight:700;line-height:48px;text-align:center;letter-spacing:.5px}

/* proven */
.person{left:120px;top:2290px;width:340px;height:370px;background:linear-gradient(180deg,#f3f5f8 0%,#cfd8e3 60%,#7a8aa0 100%)}
.proven-title{left:560px;top:2330px;width:520px;font-size:28px;line-height:38px;font-weight:700;color:var(--blue)}
.proven-copy{left:560px;top:2440px;width:520px;font-size:14px;line-height:22px}
.proven-copy p{margin-bottom:20px}

/* clients */
.clients{left:0;top:2660px;width:1200px;height:220px;background:var(--grey-band)}
.client{top:2752px;font-size:26px;font-weight:600;color:#6b7582}
.client-badge{left:1000px;top:2740px;width:50px;height:60px;background:#6b7582}

/* footer */
.footer{left:0;top:2880px;width:1200px;height:200px;background:var(--navy)}
.foot-brand{left:70px;top:2920px;color:var(--white);font-size:18px;font-weight:700;width:220px;line-height:26px}
.social{top:3010px;width:28px;height:28px;background:#2a5592}
.foot-col{top:2912px;color:var(--white);font-size:13px}
.foot-col h4{font-size:14px;font-weight:700;letter-spacing:.5px;margin-bottom:12px}
.foot-col li{list-style:none;line-height:22px}
.foot-col li::before{content:"▸ ";font-size:10px}
.contact-row{display:flex;gap:10px;align-items:flex-start;margin-bottom:12px;line-height:18px}
.news-input{width:190px;height:30px;background:var(--white);color:var(--muted);font-size:12px;padding:6px 10px;margin:12px 0}
.news-btn{width:120px;height:32px;background:var(--blue-bright);color:var(--white);font-size:13px;font-weight:700;line-height:32px;text-align:center}
.copyright{left:0;top:3080px;width:1200px;height:48px;background:var(--navy-deep);color:#c4cfdf;font-size:12px;line-height:48px;text-align:center}
</style>
</head>
<body>

<section class="abs hero" role="img" aria-label="Business meeting photograph under a blue overlay"></section>
<svg class="abs hero-notch" viewBox="0 0 1200 110" aria-hidden="true"><polygon points="0,100 600,0 1200,100 1200,110 0,110" fill="#ffffff"/></svg>

<div class="abs topbar-phone">
  <svg width="16" height="16" viewBox="0 0 24 24"><path d="M6.6 10.8a15 15 0 0 0 6.6 6.6l2.2-2.2a1 1 0 0 1 1-.25 11.4 11.4 0 0 0 3.6.57 1 1 0 0 1 1 1V20a1 1 0 0 1-1 1A17 17 0 0 1 3 4a1 1 0 0 1 1-1h3.5a1 1 0 0 1 1 1c0 1.25.2 2.45.57 3.57a1 1 0 0 1-.25 1z" fill="#fff"/></svg>
  (0400) 512 736
</div>
<div class="abs brand"><span class="brand-dot"></span>BRIGHT MERIDIAN PARTNERS</div>
<nav class="abs nav">
  <span class="active">HOME</span><span>ABOUT</span><span>SERVICES</span><span>CLIENTS</span><span>CONTACT</span>
  <svg width="16" height="16" viewBox="0 0 24 24"><circle cx="10" cy="10" r="7" stroke="#fff" stroke-width="2.5" fill="none"/><line x1="15" y1="15" x2="22" y2="22" stroke="#fff" stroke-width="2.5"/></svg>
</nav>
<h1 class="abs hero-title center">We Simply Accelerate Revenue</h1>
<p class="abs hero-sub center">Proven Experts, Proven Industry Results</p>
<div class="abs btn-outline">LEARN MORE</div>

<div class="abs welcome-mark"></div>
<h2 class="abs section-title welcome-title">WELCOME TO BRIGHT MERIDIAN PARTNERS</h2>
<div class="abs welcome-copy">
  <p>Bright Meridian Partners was founded in January 2017 so there was a closer gap in the consumer goods and services market for a boutique group of experts to support execution of strategies to accelerate revenue.</p>
  <p>We could see that Top ASX and SME businesses needed solutions to problems now. In an on demand world, clients more often did not have the resource or capability within their current business to address their problems. Coupled with a trend in the marketplace that supports the "gig" economy.</p>
</div>
<div class="abs btn-solid">LEARN MORE</div>

<section class="abs expert" role="img" aria-label="Office photograph under a deep blue overlay"></section>
<h2 class="abs expert-title">WE ARE EXPERT IN</h2>
<div class="abs skill" style="left:95px">
  <div class="skill-icon"><svg width="64" height="64" viewBox="0 0 64 64"><rect x="8" y="36" width="10" height="20" fill="#1f65b3"/><rect x="24" y="26" width="10" height="30" fill="#1f65b3"/><rect x="40" y="14" width="10" height="42" fill="#1f65b3"/></svg></div>SALES</div>
<div class="abs skill" style="left:305px">
  <div class="skill-icon"><svg width="64" height="64" viewBox="0 0 64 64"><polygon points="8,26 22,26 46,12 46,52 22,38 8,38" fill="#1f65b3"/><rect x="14" y="38" width="8" height="14" fill="#1f65b3"/></svg></div>MARKETING</div>
<div class="abs skill" style="left:515px">
  <div class="skill-icon"><svg width="64" height="64" viewBox="0 0 64 64"><circle cx="32" cy="18" r="9" fill="#1f65b3"/><path d="M16 54v-10a16 16 0 0 1 32 0v10z" fill="#1f65b3"/></svg></div>LEADERSHIP</div>
<div class="abs skill" style="left:725px">
  <div class="skill-icon"><svg width="64" height="64" viewBox="0 0 64 64"><rect x="8" y="10" width="48" height="30" fill="none" stroke="#1f65b3" stroke-width="4"/><circle cx="22" cy="48" r="6" fill="#1f65b3"/><path d="M12 60a10 10 0 0 1 20 0z" fill="#1f65b3"/></svg></div>COACHING</div>
<div class="abs skill" style="left:935px">
  <div class="skill-icon"><svg width="64" height="64" viewBox="0 0 64 64"><rect x="6" y="20" width="32" height="24" fill="#1f65b3"/><polygon points="38,26 50,26 58,36 58,44 38,44" fill="#1f65b3"/><circle cx="16" cy="48" r="6" fill="#fff" stroke="#1f65b3" stroke-width="3"/><circle cx="48" cy="48" r="6" fill="#fff" stroke="#1f65b3" stroke-width="3"/></svg></div>SUPPLY CHAIN</div>

<section class="abs quote-band" role="img" aria-label="Soft grey architectural photograph"></section>
<svg class="abs arrow" style="left:20px;top:1490px" viewBox="0 0 30 50"><polyline points="22,6 8,25 22,44" fill="none" stroke="#fff" stroke-width="4"/></svg>
<svg class="abs arrow" style="right:20px;top:1490px" viewBox="0 0 30 50"><polyline points="8,6 22,25 8,44" fill="none" stroke="#fff" stroke-width="4"/></svg>
<div class="abs quote-mark">&ldquo;</div>
<blockquote class="abs quote-text">"Agility is the key to building a business that is faster and more profitable than the competition"</blockquote>
<div class="abs quote-author">&mdash; Dana Whitlock</div>

<h2 class="abs section-title services-title">SERVICES WE PROVIDE YOU</h2>
<p class="abs services-sub">Bright Meridian Partners will help you win</p>
<p class="abs services-copy">Whether you have the need to unlock the strategic vision to keep pace in the market, improve your customer and consumer relevance, help make the business more fit for an agile future, simplify the processes to get focus, within the reg, you go to market, our experts can deliver.</p>

<div class="abs tile" style="left:0;background:linear-gradient(135deg,#e9edf2,#a9b6c6)" role="img" aria-label="Photograph of growth charts and financial reports"></div>
<div class="abs tile" style="left:400px;background:linear-gradient(135deg,#5f8fc8,#1d4c8c)" role="img" aria-label="Illustration of a connected customer network"></div>
<div class="abs tile" style="left:800px;background:linear-gradient(135deg,#c8d0da,#55677f)" role="img" aria-label="Photograph of a team of business people"></div>
<div class="abs tile-label" style="left:0">STRATEGIC FOCUS</div>
<div class="abs tile-label" style="left:400px">CUSTOMER FOCUS</div>
<div class="abs tile-label" style="left:800px">CONSUMER FOCUS</div>

<div class="abs person" role="img" aria-label="Photograph of a businesswoman with colleagues in the background"></div>
<h2 class="abs proven-title">We are proven experts in the Consumer Products and Services Mktplace</h2>
<div class="abs proven-copy">
  <p>SOME of our Clients come to us to help embed leadership or unlock their Strategic Vision to keep pace in an ever-changing marketplace.</p>
  <p>MOST of our clients come to us to implement global and practice planning, systems and processes with the teams to accelerate performance.</p>
  <p>ALL of our clients want us to help to coach and build high performing teams and transfer capability to future proof their business.</p>
</div>

<section class="abs clients"></section>
<svg class="abs arrow" style="left:20px;top:2745px" viewBox="0 0 30 50"><polyline points="22,6 8,25 22,44" fill="none" stroke="#6b7582" stroke-width="4"/></svg>
<svg class="abs arrow" style="right:20px;top:2745px" viewBox="0 0 30 50"><polyline points="8,6 22,25 8,44" fill="none" stroke="#6b7582" stroke-width="4"/></svg>
<div class="abs client" style="left:90px">Veltrona</div>
<div class="abs client" style="left:280px">Corvadis</div>
<div class="abs client" style="left:470px">Solmere</div>
<div class="abs client" style="left:660px;top:2740px;font-size:20px;line-height:26px;width:150px">Harwell<br>Care Trust</div>
<div class="abs client" style="left:840px">Nortavo</div>
<div class="abs client-badge"></div>

<footer class="abs footer"></footer>
<div class="abs foot-brand">BRIGHT MERIDIAN<br>PARTNERS</div>
<div class="abs social" style="left:130px"></div>
<div class="abs social" style="left:166px"></div>
<div class="abs social" style="left:202px"></div>

<div class="abs foot-col" style="left:350px">
  <h4>SITEMAP</h4>
  <ul><li>Home</li><li>About</li><li>Services</li><li>Clients</li><li>Contact</li></ul>
</div>
<div class="abs foot-col" style="left:600px;width:260px">
  <h4>CONTACT US</h4>
  <div class="contact-row"><svg width="14" height="16" viewBox="0 0 24 24"><path d="M12 2a7 7 0 0 0-7 7c0 5 7 13 7 13s7-8 7-13a7 7 0 0 0-7-7zm0 9.5A2.5 2.5 0 1 1 12 6.5a2.5 2.5 0 0 1 0 5z" fill="#fff"/></svg><span>BRIGHT MERIDIAN PARTNERS<br>Bright Meridian Partners Pty Ltd<br>Harbour Row<br>NSW 2000</span></div>
  <div class="contact-row"><svg width="14" height="14" viewBox="0 0 24 24"><path d="M6.6 10.8a15 15 0 0 0 6.6 6.6l2.2-2.2a1 1 0 0 1 1-.25 11.4 11.4 0 0 0 3.6.57 1 1 0 0 1 1 1V20a1 1 0 0 1-1 1A17 17 0 0 1 3 4a1 1 0 0 1 1-1h3.5a1 1 0 0 1 1 1c0 1.25.2 2.45.57 3.57a1 1 0 0 1-.25 1z" fill="#fff"/></svg><span>(0400) 512 736</span></div>
  <div class="contact-row"><svg width="14" height="12" viewBox="0 0 24 18"><rect x="1" y="1" width="22" height="16" fill="none" stroke="#fff" stroke-width="2"/><polyline points="1,1 12,10 23,1" fill="none" stroke="#fff" stroke-width="2"/></svg><span>info@brightmeridianpartners.example</span></div>
</div>
<div class="abs foot-col" style="left:920px;width:220px">
  <h4>NEWSLETTER</h4>
  <p style="line-height:18px">Would you like to receive exclusive access to articles &amp; regular monthly newsletters?</p>
  <div class="news-input">Enter Name</div>
  <div class="news-btn">SUBSCRIBE</div>
</div>
<div class="abs copyright">© BRIGHT MERIDIAN PARTNERS - 2017 All Rights Reserved</div>

</body>
</html>
```